Frostvale Cold Packs needs stationery designed for their new logo

We have a new logo so now want all our stationery to be redesigned.
Frostvale is a gel ice pack product used by the seafood & food industry to transport chilled products around the world.

We would like to use our new logo with icy or snow backgrounds or elements.
Our company tag line is "Keep your products chilled for longer"
I'll attach our old business cards so that you can use the text off them.
2nd attachment is our new logo to be used.

We want a design for:
- Business cards
- Letter Head
- Email signature

Target Market(s)

seafood & chilled food distributors

Industry/Entity Type

Industry

Font styles to use
Sans Serif

Colors
0492cd
85cae6
cee9f5

Requirements
Must have
• Our logo
Nice to have
• Snow or ice background or image incorporated somehow

```html
<!DOCTYPE html>
<html lang="en">
<head>
<meta charset="utf-8">
<title>Frostvale Cold Packs – Business Cards</title>
<link href="https://fonts.googleapis.com/css2?family=Montserrat:wght@500;600;700&family=Roboto:wght@400;500&display=swap" rel="stylesheet">
<style>
  :root {
    --brand-blue: #0492cd;
    --mid-blue: #85cae6;
    --pale-blue: #cee9f5;
    --ink: #1d1d1f;
    --logo-grey: #6d6f73;
    --backdrop: #ece6d3;
    --card-white: #ffffff;
  }
  * { box-sizing: border-box; margin: 0; padding: 0; }
  html, body { width: 1200px; height: 1200px; overflow: hidden; }
  body {
    background: var(--backdrop);
    font-family: "Roboto", Arial, sans-serif;
    color: var(--ink);
    position: relative;
  }
  .card {
    position: absolute;
    left: 150px;
    width: 900px;
    height: 514px;
    background: var(--card-white);
    overflow: hidden;
    box-shadow: 0 10px 30px rgba(80, 70, 40, 0.18);
  }
  .card--snow { top: 56px; }
  .card--ice { top: 630px; }

  /* Snow front */
  .snow-art {
    position: absolute;
    inset: 0 0 80px 0;
    background: linear-gradient(180deg, var(--pale-blue) 0%, #e4f3fa 45%, #ffffff 100%);
  }
  .card-name {
    font-family: "Montserrat", sans-serif;
    font-weight: 700;
    color: var(--brand-blue);
    font-size: 34px;
    letter-spacing: 0.5px;
  }
  .card-role {
    font-family: "Montserrat", sans-serif;
    font-weight: 500;
    font-size: 20px;
    color: var(--ink);
    margin-top: 4px;
  }
  .card--snow .identity { position: absolute; left: 60px; top: 64px; }
  .logo {
    position: absolute;
    display: flex;
    align-items: center;
    gap: 14px;
  }
  .logo-dot {
    width: 46px; height: 46px;
    border-radius: 50%;
    background: var(--brand-blue);
  }
  .logo-word {
    font-family: "Montserrat", sans-serif;
    font-weight: 700;
    color: var(--logo-grey);
    font-size: 44px;
  }
  .card--snow .logo { right: 60px; top: 52px; }
  .contact {
    position: absolute;
    list-style: none;
    font-family: "Montserrat", sans-serif;
    font-weight: 500;
    font-size: 19px;
    color: var(--ink);
  }
  .contact li { display: flex; align-items: center; gap: 14px; line-height: 30px; }
  .contact svg { width: 20px; height: 20px; flex: none; }
  .card--snow .contact { left: 60px; top: 340px; }
  .tagline-band {
    position: absolute;
    left: 0; right: 0; bottom: 0;
    height: 80px;
    background: var(--brand-blue);
    color: #fff;
    font-size: 28px;
    display: flex;
    align-items: center;
    justify-content: center;
    letter-spacing: 0.3px;
  }

  /* Ice front */
  .card--ice .identity { position: absolute; left: 60px; top: 70px; }
  .card--ice .contact { left: 440px; top: 62px; }
  .ice-art {
    position: absolute;
    left: 0; right: 0; bottom: 0;
    height: 300px;
    background: linear-gradient(160deg, #a9d6ee 0%, var(--mid-blue) 40%, #b9def1 70%, var(--pale-blue) 100%);
  }
  .card--ice .logo { left: 50%; transform: translateX(-50%); top: 280px; }
  .card--ice .logo-word { font-size: 56px; }
  .card--ice .logo-dot { width: 56px; height: 56px; }
  .ice-tagline {
    position: absolute;
    left: 0; right: 0; top: 390px;
    text-align: center;
    font-family: "Montserrat", sans-serif;
    font-weight: 600;
    font-size: 30px;
    color: var(--ink);
  }
</style>
</head>
<body>

<section class="card card--snow" aria-label="Business card front, snow design">
  <div class="snow-art" role="img" aria-label="Pale blue snowfall of scattered snowflakes across the upper card"></div>
  <div class="identity">
    <h1 class="card-name">Marlow Keane</h1>
    <p class="card-role">Business Development</p>
  </div>
  <div class="logo">
    <span class="logo-dot"></span>
    <span class="logo-word">Frostvale</span>
  </div>
  <ul class="contact">
    <li>
      <svg viewBox="0 0 20 20" aria-hidden="true"><rect x="1" y="5" width="18" height="12" rx="1.5" fill="#0492cd"/><path d="M1 6 L10 12 L19 6" stroke="#fff" stroke-width="1.6" fill="none"/></svg>
      marlow.keane@frostvale.com.au
    </li>
    <li>
      <svg viewBox="0 0 20 20" aria-hidden="true"><circle cx="10" cy="10" r="8.5" fill="none" stroke="#0492cd" stroke-width="1.6"/><ellipse cx="10" cy="10" rx="3.6" ry="8.5" fill="none" stroke="#0492cd" stroke-width="1.4"/><path d="M1.5 10 H18.5 M3 5.5 H17 M3 14.5 H17" stroke="#0492cd" stroke-width="1.4"/></svg>
      www.frostvale.com.au
    </li>
  </ul>
  <div class="tagline-band">Keep your products chilled for longer</div>
</section>

<section class="card card--ice" aria-label="Business card front, ice design">
  <div class="identity">
    <h2 class="card-name">Marlow Keane</h2>
    <p class="card-role">Business Development</p>
  </div>
  <ul class="contact">
    <li>
      <svg viewBox="0 0 20 20" aria-hidden="true"><rect x="1" y="5" width="18" height="12" rx="1.5" fill="#0492cd"/><path d="M1 6 L10 12 L19 6" stroke="#fff" stroke-width="1.6" fill="none"/></svg>
      marlow.keane@frostvale.com.au
    </li>
    <li>
      <svg viewBox="0 0 20 20" aria-hidden="true"><circle cx="10" cy="10" r="8.5" fill="none" stroke="#0492cd" stroke-width="1.6"/><ellipse cx="10" cy="10" rx="3.6" ry="8.5" fill="none" stroke="#0492cd" stroke-width="1.4"/><path d="M1.5 10 H18.5 M3 5.5 H17 M3 14.5 H17" stroke="#0492cd" stroke-width="1.4"/></svg>
      www.frostvale.com.au
    </li>
  </ul>
  <div class="ice-art" role="img" aria-label="Cracked blue ice texture filling the lower card"></div>
  <div class="logo">
    <span class="logo-dot"></span>
    <span class="logo-word">Frostvale</span>
  </div>
  <p class="ice-tagline">Keep your products chilled for longer</p>
</section>

</body>
</html>
```